PowerPoint Template - Korvel Mint

You find in the attached file a short description of our firm, logo, mission, vision and values. We made an empty template in order to let you free to imagine. We-have high expectations on ideas "out of the box" to merge our job (consulting firm) with Zen concept. We really Would like "Zen" look and feel, to show our difference. And we want to avoid "standard consulting" (smart guys with ties, shaking hand with Brimlo smilies ...) Thank you

Target Market(s)

organization (Rather big ones)

Industry/Entity Type

Consulting

Number of Pages Required

3 page

Font styles to use
Sans Serif

Requirements
Must have
• - Some nice pictures - Be really "Zen" (quiet, smart, luxury, people centric)
Should not have
• really looks like "standard consulting" (smart guys with ties, shaking hand with Brimlo smilies ...)

```html
<!DOCTYPE html>
<html lang="en">
<head>
<meta charset="utf-8">
<title>Korvel Mint – Presentation Template</title>
<link rel="stylesheet" href="https://fonts.googleapis.com/css2?family=Open+Sans:wght@400;600;700;800&display=swap">
<style>
:root{
  --stage:#9b9b9b;
  --orange:#ea6d1e;
  --orange-soft:#f08a3c;
  --amber:#f9a51f;
  --green:#8cc63f;
  --green-soft:#c5e0a5;
  --grey-block:#dfe5e8;
  --ink:#1b1b1b;
  --text:#333;
  --muted:#8a8a8a;
  --white:#fff;
}
*{box-sizing:border-box;margin:0;padding:0}
html,body{width:1000px;height:1200px;overflow:hidden}
body{background:var(--stage);font-family:"Open Sans",Arial,sans-serif;color:var(--text);position:relative}
.slide{position:absolute;width:478px;height:355px;background:var(--white);overflow:hidden}
.s-cover{left:22px;top:28px}
.s-activity{left:510px;top:28px}
.s-name{left:22px;top:397px}
.s-paradox{left:510px;top:397px}
.s-mvv{left:22px;top:762px}
.s-cloud{left:510px;top:762px}

/* shared header / footer */
.slide-title{position:absolute;left:30px;top:12px;font-size:12.5px;font-weight:400;color:var(--orange);letter-spacing:.3px}
.slide-sub{position:absolute;left:30px;top:30px;font-size:5.5px;color:var(--muted)}
.header-rule{position:absolute;left:30px;top:40px;width:360px;height:1px;background:linear-gradient(90deg,var(--green),rgba(140,198,63,.15))}
.brand{position:absolute;right:14px;top:12px;display:flex;flex-direction:column;align-items:center;gap:2px}
.brand-dot{width:18px;height:18px;border-radius:50%;border:2px solid var(--orange)}
.brand-name{font-size:5px;color:var(--orange);letter-spacing:1px;font-weight:600}
.footer-band{position:absolute;left:0;bottom:8px;width:440px;height:8px;background:linear-gradient(90deg,#cfe7b0,var(--green) 30%);clip-path:polygon(0 0,100% 0,96% 100%,0 100%)}
.page-tab{position:absolute;right:0;bottom:4px;width:44px;height:16px;background:var(--orange);color:var(--white);font-size:9px;text-align:center;line-height:16px}

/* cover */
.cover-top{position:absolute;left:0;top:0;width:100%;height:124px;background:var(--white)}
.cover-body{position:absolute;left:0;top:124px;width:100%;height:231px;background:var(--orange);color:var(--white);text-align:center}
.cover-brand{position:absolute;left:0;top:32px;width:100%;display:flex;flex-direction:column;align-items:center;gap:6px}
.cover-brand .brand-dot{width:40px;height:40px;border-width:3px}
.cover-brand .brand-name{font-size:9px;letter-spacing:3px;font-weight:400}
.cover-title{margin-top:24px;font-size:23px;line-height:29px;font-weight:400}
.cover-kicker{font-size:8px;font-weight:700;margin-top:6px}
.cover-date{font-size:9px;font-weight:700;margin-top:7px}
.cover-legal{position:absolute;bottom:16px;width:100%;font-size:5px}

/* activity */
.facts{position:absolute;left:46px;top:72px;width:400px;list-style:none}
.fact{display:flex;gap:12px;margin-bottom:11px}
.fact-icon{flex:none;width:24px;height:22px;border-radius:4px;position:relative;background:var(--orange)}
.fact-icon.green{background:var(--green)}
.fact-icon::after{content:"";position:absolute;left:5px;top:4px;width:14px;height:14px;border-radius:50%;background:var(--white)}
.fact h3{font-size:8px;font-weight:700;color:var(--ink)}
.fact p,.fact li{font-size:5.3px;line-height:7.5px;color:var(--text);margin-left:8px}
.fact ul{list-style:disc;margin-left:14px}

/* name explanation */
.photo{position:absolute;left:0;top:0;width:222px;height:355px;background:linear-gradient(180deg,#c9d6e2 0%,#a9b5bf 55%,#6f6e64 78%,#4a4a44 100%)}
.name-panel{position:absolute;left:222px;top:0;right:0;bottom:0;background:var(--orange);color:var(--white)}
.name-panel .slide-title,.name-panel .slide-sub{color:var(--white);left:36px}
.name-group{position:absolute;left:36px;display:flex;gap:14px}
.name-num{width:16px;height:16px;border:1.3px solid var(--white);border-radius:50%;font-size:9px;text-align:center;line-height:14px;flex:none}
.name-group ul{list-style:disc;margin-left:8px;font-size:9px;line-height:13.5px;width:150px}

/* mission vision value */
.mvv-art{position:absolute;inset:0}
.mvv-heading{position:absolute;font-size:27px;font-weight:800;color:var(--ink);letter-spacing:.3px}
.mission-text{position:absolute;left:38px;top:76px;width:180px;font-size:5.5px;line-height:7px;color:var(--ink)}
.vision-text{position:absolute;left:242px;top:64px;width:164px;font-size:5.6px;line-height:7.2px;text-align:justify;color:var(--ink)}
.value-list{position:absolute;top:224px;list-style:disc;font-size:7.5px;line-height:11.3px;color:var(--ink)}
</style>
</head>
<body>

<!-- cover -->
<section class="slide s-cover">
  <div class="cover-top"></div>
  <div class="cover-brand">
    <span class="brand-dot"></span>
    <span class="brand-name">KORVEL MINT</span>
  </div>
  <div class="cover-body">
    <h1 class="cover-title">KORVEL MINT<br>PPT TEMPLET</h1>
    <p class="cover-kicker">Request for Proposal</p>
    <p class="cover-date">JUNE 2016</p>
    <p class="cover-legal">© Korvel Mint - CONFIDENTIEL</p>
  </div>
</section>

<!-- activity and context -->
<section class="slide s-activity">
  <h2 class="slide-title">ACTIVITY AND CONTEXT</h2>
  <p class="slide-sub">Insert your sub title here</p>
  <div class="header-rule"></div>
  <div class="brand"><span class="brand-dot"></span><span class="brand-name">KORVEL MINT</span></div>
  <ul class="facts">
    <li class="fact"><span class="fact-icon"></span><div><h3>Korvel Mint</h3><p>Korvel Mint is a management, organization and performance improvement consulting firm</p></div></li>
    <li class="fact"><span class="fact-icon green"></span><div><h3>Our convictions</h3><p>in a hyper competitive environment, only organizations able to quickly adapt will survive. Digital companies will have a competitive advantage because they will understand their ecosystem better, faster and will act more effectively than others</p></div></li>
    <li class="fact"><span class="fact-icon"></span><div><h3>Our mission</h3><p>is to support the digital transformation of our clients</p></div></li>
    <li class="fact"><span class="fact-icon green"></span><div><h3>Our differences</h3><ul><li>Use Lean and Agile known methods in innovative ways, creating quickly measurable value</li><li>Avoid stress and permanent emergency, accept mistakes to bounce back quickly</li></ul></div></li>
  </ul>
  <div class="footer-band"></div><div class="page-tab">02</div>
</section>

<!-- name explanation -->
<section class="slide s-name">
  <div class="photo" role="img" aria-label="Photograph of city towers beside a river under a pale sky"></div>
  <div class="name-panel">
    <h2 class="slide-title" style="top:16px">NAME EXPLANATION</h2>
    <p class="slide-sub" style="top:34px">Insert your sub title here</p>
    <div class="name-group" style="top:92px"><span class="name-num">1</span>
      <ul><li>No stress</li><li>Respect</li><li>Human centric</li><li>Accept mistakes</li></ul></div>
    <div class="name-group" style="top:172px"><span class="name-num">2</span>
      <ul><li>Value for customers and for ourselves</li><li>Value by action</li><li>Quick Value</li><li>Measurable value</li></ul></div>
  </div>
</section>

<!-- paradoxes -->
<section class="slide s-paradox">
  <h2 class="slide-title">PARADOXES WE DEFEND</h2>
  <p class="slide-sub">Insert your sub title here</p>
  <div class="header-rule"></div>
  <div class="brand"><span class="brand-dot"></span><span class="brand-name">KORVEL MINT</span></div>
  <svg class="petals" width="478" height="355" viewBox="0 0 478 355" style="position:absolute;left:0;top:0" font-family="Open Sans, sans-serif">
    <defs><path id="petal" d="M0,-4 C-18,-24 -42,-44 -42,-72 A42 42 0 1 1 42,-72 C42,-44 18,-24 0,-4 Z"/></defs>
    <g transform="translate(245,210)">
      <use href="#petal" fill="var(--green)" transform="rotate(-30)"/>
      <use href="#petal" fill="var(--orange)" transform="rotate(30)"/>
      <use href="#petal" fill="var(--green)" transform="rotate(90)"/>
      <use href="#petal" fill="var(--orange)" transform="rotate(150)"/>
      <use href="#petal" fill="var(--green)" transform="rotate(210)"/>
      <use href="#petal" fill="var(--orange)" transform="rotate(270)"/>
    </g>
    <g fill="#fff" font-size="6.5" text-anchor="middle">
      <text x="209" y="143">Zen and</text><text x="209" y="152">Digital</text>
      <text x="281" y="143">Zen and</text><text x="281" y="152">Quick</text>
      <text x="317" y="207">Zen and</text><text x="317" y="216">Action</text>
      <text x="281" y="271">Value and</text><text x="281" y="280">Measurable</text>
      <text x="209" y="271">Value and</text><text x="209" y="280">Quick</text>
      <text x="172" y="199">Customers and</text><text x="172" y="208">Employees,</text><text x="172" y="217">both first</text>
    </g>
    <g fill="#fff" font-size="9" text-anchor="middle">
      <text x="229" y="180">01</text><text x="262" y="180">02</text><text x="278" y="213">03</text>
      <text x="262" y="247">04</text><text x="229" y="247">05</text><text x="212" y="213">06</text>
    </g>
  </svg>
  <div class="footer-band"></div><div class="page-tab">02</div>
</section>

<!-- mission vision value -->
<section class="slide s-mvv">
  <svg class="mvv-art" width="478" height="355" viewBox="0 0 478 355">
    <rect x="0" y="0" width="250" height="160" fill="var(--green)"/>
    <rect x="30" y="0" width="40" height="40" fill="var(--green-soft)"/>
    <rect x="110" y="20" width="40" height="40" fill="var(--green-soft)"/>
    <rect x="150" y="60" width="40" height="40" fill="#a9d374"/>
    <rect x="190" y="0" width="60" height="40" fill="#d9ecc4"/>
    <rect x="0" y="100" width="40" height="40" fill="#a9d374"/>
    <rect x="70" y="120" width="40" height="40" fill="var(--green-soft)"/>
    <rect x="190" y="100" width="60" height="60" fill="#d9ecc4"/>
    <rect x="280" y="0" width="40" height="30" fill="var(--grey-block)"/>
    <rect x="380" y="20" width="50" height="40" fill="var(--grey-block)"/>
    <rect x="430" y="120" width="48" height="50" fill="var(--grey-block)"/>
    <rect x="300" y="190" width="60" height="50" fill="var(--grey-block)"/>
    <rect x="400" y="230" width="50" height="50" fill="#eef1f3"/>
    <rect x="330" y="290" width="60" height="50" fill="var(--grey-block)"/>
    <rect x="0" y="160" width="270" height="195" fill="var(--amber)"/>
    <rect x="0" y="200" width="40" height="40" fill="var(--orange)"/>
    <rect x="110" y="160" width="50" height="40" fill="#fbc05a"/>
    <rect x="200" y="200" width="70" height="60" fill="var(--orange-soft)"/>
    <rect x="40" y="280" width="60" height="50" fill="var(--orange)"/>
    <rect x="150" y="300" width="50" height="55" fill="#f7941d"/>
    <rect x="230" y="280" width="40" height="40" fill="var(--orange)"/>
    <rect x="270" y="240" width="30" height="40" fill="#fbc05a"/>
  </svg>
  <h2 class="mvv-heading" style="left:36px;top:28px">MISSION</h2>
  <p class="mission-text">Support our customers in their digital transformation with agile and innovative approaches results oriented</p>
  <h2 class="mvv-heading" style="left:240px;top:20px">VISION</h2>
  <p class="vision-text">Organizational transformations are often made with top-down approaches, which require significant lead times.<br>The vagaries of time, complexity, context uncertainty make it almost impossible ROI measurement. Furthermore, backtracking are difficult and expensive.<br>To address these weaknesses, we propose an innovative approach with short cycle, in which the results of each step of the transformation can be measured quickly and quantitatively. This approach also allows to adjust the direction progressively according to obtained results.</p>
  <h2 class="mvv-heading" style="left:36px;top:180px">VALUE</h2>
  <ul class="value-list" style="left:46px"><li>People centric</li><li>Honesty / caring</li><li>Open mind</li><li>Anticipation</li><li>Customer focus</li><li>Well-being</li><li>Engagement</li></ul>
  <ul class="value-list" style="left:145px;width:80px"><li>Pragmatism</li><li>Direct to the point</li><li>Little, quick and perfect</li><li>Pride</li></ul>
</section>

<!-- cloud tag -->
<section class="slide s-cloud">
  <h2 class="slide-title">CLOUD TAG</h2>
  <p class="slide-sub">Insert your sub title here</p>
  <div class="header-rule"></div>
  <div class="brand"><span class="brand-dot"></span><span class="brand-name">KORVEL MINT</span></div>
  <svg width="478" height="355" viewBox="0 0 478 355" style="position:absolute;left:0;top:0" font-family="Open Sans, sans-serif">
    <!-- people cloud -->
    <g>
      <path d="M45,95 a22,22 0 0 1 18,-28 a28,28 0 0 1 52,-8 a20,20 0 0 1 34,14 a18,18 0 0 1 0,34 h-98 a16,16 0 0 1 -6,-12 z" fill="#e7e7e7"/>
      <rect x="55" y="45" width="18" height="62" fill="var(--green)"/>
      <rect x="73" y="45" width="18" height="62" fill="var(--orange)"/>
      <rect x="91" y="45" width="18" height="62" fill="var(--green)"/>
      <rect x="109" y="45" width="18" height="62" fill="var(--orange)"/>
      <rect x="127" y="45" width="18" height="62" fill="var(--green)"/>
      <text x="100" y="70" font-size="10" font-weight="700" fill="#333" text-anchor="middle">People</text>
      <g font-size="8" fill="#fff" text-anchor="middle">
        <path d="M55,98 h20 v22 l-10,5 l-10,-5z" fill="var(--orange)"/><text x="65" y="113">01</text>
        <path d="M79,104 h20 v22 l-10,5 l-10,-5z" fill="var(--green)"/><text x="89" y="119">02</text>
        <path d="M103,98 h20 v22 l-10,5 l-10,-5z" fill="var(--orange)"/><text x="113" y="113">03</text>
        <path d="M127,104 h20 v22 l-10,5 l-10,-5z" fill="var(--green)"/><text x="137" y="119">04</text>
      </g>
      <g font-size="7.5" fill="#333" text-anchor="middle">
        <text x="56" y="136">Serenity</text><text x="85" y="149">Respect</text><text x="113" y="142">Open</text><text x="147" y="149">Trust</text>
      </g>
    </g>
    <!-- vision cloud -->
    <g>
      <circle cx="395" cy="75" r="22" fill="var(--green)"/>
      <circle cx="420" cy="90" r="18" fill="var(--green)"/>
      <circle cx="370" cy="92" r="26" fill="var(--orange)"/>
      <circle cx="400" cy="100" r="22" fill="var(--orange)"/>
      <rect x="350" y="95" width="70" height="25" rx="12" fill="var(--orange)"/>
      <circle cx="305" cy="95" r="22" fill="var(--orange-soft)"/>
      <circle cx="325" cy="85" r="20" fill="var(--amber)"/>
      <rect x="285" y="95" width="55" height="22" rx="11" fill="var(--amber)"/>
      <text x="312" y="102" font-size="9" fill="#333" text-anchor="middle">Early</text>
      <text x="385" y="106" font-size="10" font-weight="600" fill="#333" text-anchor="middle">Vision</text>
      <text x="402" y="75" font-size="9" fill="#333" text-anchor="middle">360°</text>
    </g>
    <!-- action cloud -->
    <g>
      <rect x="128" y="168" width="190" height="100" rx="40" fill="#fff" stroke="#d7d7d7" stroke-width="4"/>
      <path d="M180,168 a24,24 0 0 1 24,-24 h40 v48 h-64z" fill="#fff"/>
      <rect x="206" y="146" width="38" height="28" rx="6" fill="#98c162"/>
      <text x="225" y="158" font-size="8" fill="#333" text-anchor="middle">01</text>
      <text x="225" y="170" font-size="7.5" fill="#333" text-anchor="middle">Pragmatism</text>
      <path d="M246,146 h16 a22,22 0 0 1 22,22 v10 h-38z" fill="var(--amber)"/>
      <text x="262" y="160" font-size="8" fill="#fff">02</text><text x="270" y="173" font-size="7.5" fill="#333" text-anchor="middle">Quick</text>
      <path d="M170,176 h74 v40 h-112 v-6 a34,34 0 0 1 38,-34z" fill="var(--orange)"/>
      <text x="210" y="190" font-size="8" fill="#fff">03</text><text x="162" y="208" font-size="7.5" fill="#333" text-anchor="middle">Commitment</text>
      <rect x="246" y="180" width="60" height="36" fill="var(--green-soft)"/>
      <text x="252" y="195" font-size="8" fill="#333">04</text><text x="278" y="208" font-size="7.5" fill="#333" text-anchor="middle">Measurable</text>
      <path d="M132,218 h112 v42 h-86 a26,26 0 0 1 -26,-26z" fill="var(--green)"/>
      <text x="230" y="232" font-size="8" fill="#333">05</text>
      <text x="176" y="232" font-size="7.5" fill="#333" text-anchor="middle">Customer value</text>
      <text x="176" y="242" font-size="7.5" fill="#333" text-anchor="middle">oriented</text>
      <path d="M246,218 h60 v20 a22,22 0 0 1 -22,22 h-38z" fill="var(--amber)"/>
      <text x="252" y="232" font-size="8" fill="#fff">06</text><text x="278" y="245" font-size="7.5" fill="#333" text-anchor="middle">Meaningful</text>
      <text x="228" y="283" font-size="9.5" font-weight="700" fill="#333" text-anchor="middle">Action</text>
    </g>
  </svg>
  <div class="footer-band"></div><div class="page-tab">02</div>
</section>

</body>
</html>
```